Pinecrest Premier Motors *

Professional business cards for our auto wholesale dealership.

Target Market(s)

New and used cars sales managers and middle class to higher end private party buyers.

Industry/Entity Type

Automotive

Contact Information for Business Card

Pinecrest Premier Motors
Marcus T Holloran
Owner
(555) 014-3862
pineprem@mailvista.example
Dealer Lic # 48265

Logo Text

Pinecrest Premier Motors, Pine Prem Motors, PPM, etc

Font styles to use
Serif
Sans Serif

Colors

Designer to choose colors to be used in the design.

Requirements
Must have
• A professional, but not pretentious, look
Nice to have
• It might be nice to see "PPM" in a shape form i.e. circle, triangle, etc in the corner or background somehwere
Should not have
• bright "girly" colors

```html
<!DOCTYPE html>
<html lang="en">
<head>
<meta charset="utf-8">
<title>Pinecrest Premier Motors — Business Card</title>
<link rel="stylesheet" href="https://fonts.googleapis.com/css2?family=Lato:wght@400;700;900&display=swap">
<style>
  :root {
    --page-bg: #e4e4e2;
    --card-black: #0b0b0b;
    --panel-grey: #2b2b2c;
    --silver-light: #eef0f2;
    --silver-mid: #b9bdc3;
    --silver-dark: #6f7378;
    --text-white: #ffffff;
    --text-grey: #a9a9a9;
    --icon-ink: #2b2b2c;
  }
  html, body {
    margin: 0;
    width: 1200px;
    height: 902px;
    overflow: hidden;
    background: var(--page-bg);
  }
  .card {
    position: absolute;
    left: 100px;
    top: 166px;
    width: 1000px;
    height: 570px;
    display: block;
    filter: drop-shadow(0 10px 24px rgba(0,0,0,0.25));
  }
  .card-text { font-family: "Lato", sans-serif; }
  .holder-name { font-weight: 900; font-size: 35px; fill: var(--text-white); letter-spacing: 0.5px; }
  .holder-role { font-weight: 700; font-size: 24px; fill: var(--text-grey); }
  .contact-line { font-weight: 400; font-size: 24px; fill: var(--text-white); }
  .brand-name { font-weight: 900; fill: var(--silver-mid); }
  .brand-name-main { font-size: 46px; letter-spacing: 4px; }
  .brand-name-sub { font-size: 20px; letter-spacing: 9px; }
  .icon-badge { fill: var(--silver-mid); }
  .icon-glyph { fill: var(--icon-ink); }
  .icon-line { fill: none; stroke: var(--icon-ink); stroke-width: 1.6; }
</style>
</head>
<body>
<svg class="card" viewBox="0 0 1000 570" xmlns="http://www.w3.org/2000/svg" role="group" aria-label="Pinecrest Premier Motors business card">
  <defs>
    <clipPath id="card-shape"><rect width="1000" height="570" rx="22" ry="22"/></clipPath>
    <linearGradient id="silver-arc" x1="0" y1="0" x2="0" y2="1">
      <stop offset="0" stop-color="var(--silver-dark)"/>
      <stop offset="0.5" stop-color="var(--silver-light)"/>
      <stop offset="1" stop-color="var(--silver-dark)"/>
    </linearGradient>
    <linearGradient id="silver-badge" x1="0" y1="0" x2="0" y2="1">
      <stop offset="0" stop-color="var(--silver-light)"/>
      <stop offset="1" stop-color="var(--silver-dark)"/>
    </linearGradient>
  </defs>

  <g clip-path="url(#card-shape)">
    <rect class="card-base" width="1000" height="570" fill="var(--card-black)"/>
    <path class="info-panel" role="img" aria-label="Dark grey perforated texture panel"
          d="M0,0 H516 Q385,285 514,570 H0 Z" fill="var(--panel-grey)"/>
    <path class="divider-arc" d="M516,0 Q385,285 514,570 Q405,285 516,0 Z" fill="url(#silver-arc)"/>
    <circle class="edge-tab" cx="0" cy="128" r="18" fill="url(#silver-badge)"/>
  </g>

  <g class="card-text">
    <text class="holder-name" x="51" y="139">MARCUS T HOLLORAN</text>
    <text class="holder-role" x="51" y="168">Owner</text>

    <g class="contact-phone">
      <rect class="icon-badge" x="51" y="340" width="24" height="24" rx="4"/>
      <path class="icon-glyph" d="M56,345 q2,-1 4,0 l2,4 q0,1 -1,2 l-1,1 q2,4 6,6 l1,-1 q1,-1 2,-1 l4,2 q1,2 0,4 q-2,2 -5,1 q-9,-3 -12,-12 q-1,-3 0,-6 z"/>
      <text class="contact-line" x="84" y="361">(555) 014-3862</text>
    </g>
    <g class="contact-email">
      <rect class="icon-badge" x="51" y="380" width="24" height="24" rx="4"/>
      <rect class="icon-line" x="55" y="386" width="16" height="12"/>
      <path class="icon-line" d="M55,386 L63,393 L71,386"/>
      <text class="contact-line" x="84" y="401">pineprem@mailvista.example</text>
    </g>
    <text class="contact-line" x="51" y="444">Dealer Lic # 48265</text>

    <g class="brand">
      <circle class="brand-circle" cx="737" cy="210" r="82" fill="none" stroke="var(--silver-mid)" stroke-width="8"/>
      <text class="brand-name brand-name-main" x="737" y="378" text-anchor="middle">PINECREST</text>
      <text class="brand-name brand-name-sub" x="741" y="412" text-anchor="middle">PREMIER MOTORS</text>
    </g>
  </g>
</svg>
</body>
</html>
```